Black Friday Sale Social Media Graphics

Focusing on Black Friday Graphics for each of the pics attached.  So need the product pics turned into  social media graphics (square size). For the color scheme of the graphics, they should all be complementary to the product colors.
You can add any of the stock photography attached but none are required. I mainly need BOLD text that says:
Black Friday Sale
Up to $15 Off
If you wanted to add smaller text, these headlines can work:
1.	Burn Belly Fat Fast!
2.	Double Your Weight Loss With Our Supplements!
3.	Lose Weight Naturally: Ditch the Prescription Pills & Needles!
4.	Tired of Stubborn Belly Fat? Discover What Works!
5.	Melt Away Belly Fat Faster with Our Supplements!
6.	Struggling to Lose Weight? Discover the Ultimate Solution!
7.	Ready to Burn Fat Faster?

Target Market(s)
women trying to lose weight
Industry/Entity Type
health and wellness
Requirements
Must have
- the product pics attached

Nice to have
- Bold text that says: Black Friday Sale

```html
<!DOCTYPE html>
<html lang="en">
<head>
<meta charset="utf-8">
<title>Black Friday Sale – Burn Belly Fat Fast</title>
<link href="https://fonts.googleapis.com/css2?family=Archivo+Black&family=Bebas+Neue&family=Dancing+Script:wght@700&family=Oswald:wght@500;600&display=swap" rel="stylesheet">
<style>
  :root {
    --canvas-bg: #e6e6e6;
    --canvas-bg-light: #f4f4f4;
    --panel-pink: #dc9fb3;
    --panel-pink-dark: #c97d97;
    --headline-dark: #561626;
    --headline-dark-2: #7a2a3e;
    --headline-mauve: #9e5a70;
    --headline-mauve-2: #b77389;
    --script-white: #ffffff;
    --ribbon-yellow: #fff200;
    --ribbon-ink: #1b1b24;
    --band-maroon: #a8304f;
    --band-navy: #1f2233;
    --white: #ffffff;
    --photo-tone-a: #c89aa6;
    --photo-tone-b: #b98592;
    --product-white: #f6f6f6;
  }
  * { margin: 0; padding: 0; box-sizing: border-box; }
  html, body { width: 1200px; height: 1200px; overflow: hidden; }
  body {
    position: relative;
    background: radial-gradient(circle at 50% 40%, var(--canvas-bg-light), var(--canvas-bg));
    font-family: "Bebas Neue", sans-serif;
  }
  .promo-panel {
    position: absolute; left: 37px; top: 37px; width: 1124px; height: 802px;
    background: linear-gradient(135deg, var(--panel-pink) 0%, var(--panel-pink) 55%, var(--panel-pink-dark) 100%);
  }
  .model-photo {
    position: absolute; left: 735px; top: 225px; width: 360px; height: 700px;
    border-radius: 150px 150px 0 0;
    background: linear-gradient(180deg, var(--photo-tone-a), var(--photo-tone-b));
  }
  .headline {
    position: absolute; left: 72px; line-height: 0.8; z-index: 2;
    font-family: "Bebas Neue", sans-serif; letter-spacing: 2px;
  }
  .headline--black {
    top: 82px; font-size: 312px;
    background: linear-gradient(180deg, var(--headline-dark-2), var(--headline-dark));
    -webkit-background-clip: text; background-clip: text; color: transparent;
    filter: drop-shadow(3px 4px 3px rgba(60, 10, 25, 0.45));
  }
  .headline--friday {
    top: 340px; font-size: 300px; letter-spacing: 0;
    background: linear-gradient(180deg, var(--headline-mauve-2), var(--headline-mauve));
    -webkit-background-clip: text; background-clip: text; color: transparent;
    filter: drop-shadow(3px 4px 3px rgba(80, 20, 40, 0.4));
  }
  .headline--sale {
    position: absolute; left: 68px; top: 565px; z-index: 2;
    font-family: "Dancing Script", cursive; font-weight: 700; font-size: 230px; line-height: 1;
    color: var(--script-white);
    text-shadow: 3px 5px 4px rgba(90, 40, 55, 0.45);
  }
  .discount-ribbon {
    position: absolute; left: 898px; top: 55px; width: 250px; height: 280px; z-index: 3;
  }
  .discount-text {
    position: absolute; left: 898px; top: 78px; width: 250px; z-index: 4;
    text-align: center; color: var(--ribbon-ink);
    font-family: "Archivo Black", sans-serif; line-height: 1;
  }
  .discount-text .upto { font-size: 38px; display: block; }
  .discount-text .amount { font-size: 86px; display: block; letter-spacing: -2px; margin-top: 4px; }
  .discount-text .off { font-size: 34px; display: block; margin-top: 4px; }
  .product-lineup {
    position: absolute; left: 495px; top: 922px; width: 660px; height: 245px; z-index: 2;
    border-radius: 10px;
    background: linear-gradient(180deg, var(--product-white), #dcdcdc);
  }
  .tagline-top {
    position: absolute; left: 39px; top: 878px; width: 392px; height: 67px;
    background: var(--band-maroon); color: var(--white);
    font-family: "Oswald", sans-serif; font-weight: 600; font-size: 46px;
    display: flex; align-items: center; justify-content: center; letter-spacing: 0.5px;
  }
  .tagline-bottom {
    position: absolute; left: 39px; top: 945px; width: 392px; height: 216px;
    background: var(--band-navy); color: var(--white);
    font-family: "Bebas Neue", sans-serif; font-size: 230px; line-height: 1;
    display: flex; align-items: center; justify-content: center; padding-top: 14px;
  }
</style>
</head>
<body>
  <div class="promo-panel"></div>

  <div class="model-photo" role="img" aria-label="Photo of a smiling woman in a white cropped sweater pointing toward her waist"></div>

  <div class="headline headline--black">BLACK</div>
  <div class="headline headline--friday">FRIDAY</div>
  <div class="headline--sale">Sale</div>

  <svg class="discount-ribbon" viewBox="0 0 250 280" aria-hidden="true">
    <polygon points="0,0 250,0 250,280 125,225 0,280" fill="var(--ribbon-yellow)"/>
  </svg>
  <div class="discount-text">
    <span class="upto">UPTO</span>
    <span class="amount">$15</span>
    <span class="off">OFF</span>
  </div>

  <div class="tagline-top">BURN BELLY FAT</div>
  <div class="tagline-bottom">FAST!</div>

  <div class="product-lineup" role="img" aria-label="Photo of a row of white supplement bottles and spray bottles with colourful labels"></div>
</body>
</html>
```